Car rental website design for a UAE car rental company

This project is about creating a new website design for a car rental company located in Dubai (United Arab Emirates), I opened the same project a few months ago but I didn't receive a lot of appealing entries so I closed it but this time I am marking the project as guaranteed to avoid such situation again, if you have already provided a design before then please re-submit again on this project so that it is considered while reviewing all the designs

A few important things:

1- We need a simple non-complex design
2- The final deliverable would be 2 screens (PSD, JPEG ... etc), the first screen is for the home page and the second screen is for an internal page
3- The home page must have a section that end users can use to rent a car online directly from the home page instead of going into some inner pages
4- The current website is very old and not very appealing so avoid creating a similar design (www.quarvin-drive.example)
5- The name is Quarvin but the company rents normal cars (no Limousin cars will be rented) so avoid adding any fancy cars in the images/graphics used in the design, just normal end users cars
6- The expected pages would be: home, About us, Our team, Strategy, Contact us and links to social media pages
7- The attachments include the company's logo and some screens from other car rental companies that provide online rentals/payments

If you have any questions please feel free to ask and please note that we will need the designs urgently

Thanks

Target Market(s)

Dubai - United Arab Emirates

Industry/Entity Type

It Company

Number of Pages Required

2 page

Font styles to use
Sans Serif

Requirements
Must have
• Check the project details
Nice to have
Should not have

```html
<!DOCTYPE html>
<html lang="en">
<head>
<meta charset="utf-8">
<title>Quarvin – Rent a Car</title>
<link rel="stylesheet" href="https://fonts.googleapis.com/css2?family=Open+Sans:wght@400;600&family=Montserrat:wght@500;600&display=swap">
<style>
:root{
  --maroon:#a5003a;
  --maroon-dark:#8a0030;
  --sage:#a9b6ae;
  --ink:#333;
  --muted:#5a6460;
  --field-border:#d5d8d6;
  --white:#fff;
}
*{box-sizing:border-box;margin:0;padding:0}
html,body{width:1200px;height:900px;overflow:hidden;background:var(--white)}
body{position:relative;font-family:"Open Sans",Arial,sans-serif;color:var(--ink)}
.abs{position:absolute}

/* hero */
.hero{left:0;top:0;width:1200px;height:562px;
  background:
    radial-gradient(ellipse 520px 420px at 1010px 300px,#c9d6e4 0%,#6e8195 35%,transparent 70%),
    radial-gradient(ellipse 420px 380px at 760px 420px,#2a3848 0%,transparent 70%),
    linear-gradient(100deg,#8e9395 0%,#5f6e7b 40%,#2a3746 70%,#1e2a36 100%)}
.header-band{left:0;top:0;width:1200px;height:122px;background:rgba(70,75,78,.55)}
.top-strip{left:0;top:0;width:1200px;height:32px;background:rgba(40,44,46,.35)}

.phone{left:678px;top:7px;display:flex;align-items:center;gap:10px;color:var(--white);font-size:14px;white-space:nowrap}
.account{left:808px;top:4px;width:244px;height:24px;background:rgba(40,44,48,.85);border-radius:3px;
  color:var(--white);font-size:13px;display:flex;align-items:center;padding-left:16px;gap:8px;white-space:nowrap}
.account small{font-size:10.5px}
.search{left:1064px;top:8px}

.brand{left:119px;top:12px}
.brand-mark{position:absolute;left:40px;top:0;width:50px;height:56px;border:3px solid var(--maroon);background:rgba(255,255,255,.85)}
.brand-name{position:absolute;left:0;top:60px;font-size:26px;font-weight:600;color:#d6d9d6;letter-spacing:.5px;white-space:nowrap;line-height:30px}
.brand-tag{position:absolute;left:24px;top:88px;font-size:11px;color:var(--maroon);letter-spacing:3px;white-space:nowrap}

.main-nav{left:470px;top:69px}
.nav-item{position:absolute;top:0;height:41px;line-height:41px;font-size:15px;color:#1e2a2a;text-align:center;letter-spacing:.2px;white-space:nowrap}
.nav-item.active{color:var(--white)}

/* booking */
.booking{left:119px;top:171px;width:376px;height:322px;background:rgba(255,255,255,.88);box-shadow:0 2px 6px rgba(0,0,0,.25)}
.tab{position:absolute;top:0;height:39px;line-height:39px;text-align:center;font-size:14px;white-space:nowrap}
.tab-book{left:0;width:188px;color:var(--maroon);border-top:3px solid var(--maroon);line-height:36px;background:rgba(255,255,255,.6)}
.tab-manage{left:188px;width:188px;background:var(--sage);color:#1e2a2a}
.label{position:absolute;font-size:10px;color:var(--muted);text-transform:uppercase;letter-spacing:.2px;white-space:nowrap}
.field{position:absolute;background:var(--white);border:1px solid var(--field-border);border-radius:4px}
.placeholder{position:absolute;left:15px;top:13px;font-size:10px;color:#9aa19d;white-space:nowrap}
.link{position:absolute;right:23px;top:54px;font-size:10px;color:var(--muted);text-decoration:underline}
.checkbox{position:absolute;left:32px;top:120px;width:20px;height:20px;background:var(--white);border:1px solid var(--field-border);border-radius:3px}
.check-text{position:absolute;left:59px;top:124px;font-size:10px;color:var(--muted);white-space:nowrap}
.select-text{position:absolute;left:7px;top:13px;font-size:11px;color:#666}
.continue{position:absolute;left:256px;top:258px;width:97px;height:40px;background:var(--maroon);border-radius:4px;color:var(--white);
  font-size:12px;font-weight:600;display:flex;align-items:center;justify-content:center;gap:8px}

/* content */
.divider{left:0;top:562px;width:1200px;height:3px;background:var(--maroon)}
.welcome-head{left:119px;top:589px;width:585px;height:51px;background:#f1f1f1}
.welcome-head h1{font-family:"Montserrat",Arial,sans-serif;font-weight:500;font-size:23px;color:var(--maroon);line-height:51px;padding-left:17px}
.welcome-text{left:119px;top:655px;width:590px;font-size:13.1px;line-height:19.5px;color:var(--ink);letter-spacing:-.05px}
.welcome-text p+p{margin-top:19px}
.read-more{font-size:12px;color:var(--maroon)}

.mission{left:728px;top:565px;width:353px;height:250px;background:var(--maroon)}
.mission h2{position:absolute;left:24px;top:16px;font-family:"Montserrat",Arial,sans-serif;font-weight:600;font-size:18px;color:var(--white)}
.mission-rule{position:absolute;left:24px;top:41px;width:304px;height:2px;background:var(--white)}
.mission-photo{position:absolute;left:24px;top:61px;width:304px;height:84px;
  background:linear-gradient(90deg,#5a2a2a 0%,#c9c2bb 30%,#e8e8e8 60%,#b9bcbf 100%)}
.mission-text{position:absolute;left:24px;top:157px;width:290px;font-size:11.3px;line-height:18px;color:var(--white)}
.mission .read-more{position:absolute;right:25px;top:211px;color:#f0b7c8}

/* footer */
.footer-band{left:0;top:815px;width:1200px;height:47px;background:var(--maroon);border-top:3px solid var(--maroon-dark)}
.socials{left:119px;top:835px;display:flex;gap:10px}
.social{width:34px;height:34px;border-radius:50%;border:2px solid var(--white);background:var(--maroon);display:flex;align-items:center;justify-content:center}
.footer-nav{right:119px;top:831px;display:flex;font-size:11px;color:#f3d8e0;white-space:nowrap}
.footer-nav span.sep{margin:0 17px}
.copyright{left:0;top:872px;width:1200px;text-align:center;font-size:10px;color:var(--maroon)}
</style>
</head>
<body>

<div class="abs hero" role="img" aria-label="Close-up photograph of a dark blue car's headlight and front grille"></div>
<div class="abs header-band"></div>
<div class="abs top-strip"></div>

<div class="abs phone">
  <svg width="16" height="14" viewBox="0 0 16 14" aria-hidden="true"><path d="M1 4c0-2 3-3 7-3s7 1 7 3v1h-4V3.5H5V5H1z M3 6h10l1.5 7h-13z" fill="#fff"/><circle cx="8" cy="9.5" r="2" fill="#4a4f52"/></svg>
  <span>+971 400 5128</span>
</div>
<div class="abs account"><span>LOGIN</span><span>|</span><small>Not a member yet ?</small><span>SIGN UP</span></div>
<svg class="abs search" width="18" height="18" viewBox="0 0 18 18" aria-hidden="true"><circle cx="7" cy="7" r="5" stroke="#fff" stroke-width="2" fill="none"/><path d="M11 11l5.5 5.5" stroke="#fff" stroke-width="3" stroke-linecap="round"/></svg>

<div class="abs brand">
  <div class="brand-mark"></div>
  <div class="brand-name">Quarvin</div>
  <div class="brand-tag">Rent a Car</div>
</div>

<nav class="abs main-nav">
  <svg class="abs" style="left:0;top:0" width="612" height="41" aria-hidden="true">
    <polygon points="98,0 240,0 224,41 82,41" fill="#a9b6ae"/>
    <polygon points="238,0 360,0 344,41 222,41" fill="#a9b6ae"/>
    <polygon points="356,0 478,0 462,41 340,41" fill="#a9b6ae"/>
    <polygon points="474,0 612,0 596,41 458,41" fill="#a9b6ae"/>
    <path d="M238 0L222 41M356 0L340 41M474 0L458 41" stroke="#3a4246" stroke-width="3"/>
    <polygon points="16,0 112,0 96,41 0,41" fill="#a5003a"/>
  </svg>
  <span class="nav-item active" style="left:8px;width:102px">HOME</span>
  <span class="nav-item" style="left:92px;width:150px">ABOUT US</span>
  <span class="nav-item" style="left:226px;width:124px">OUR TEAM</span>
  <span class="nav-item" style="left:344px;width:124px">STRATEGY</span>
  <span class="nav-item" style="left:462px;width:140px">CONTACT US</span>
</nav>

<section class="abs booking" aria-label="Car booking">
  <div class="tab tab-book">Book a Car</div>
  <div class="tab tab-manage">Manage Reservation</div>

  <span class="label" style="left:32px;top:54px">Location</span>
  <span class="link">AIRPORT CODES</span>
  <div class="field" style="left:32px;top:72px;width:321px;height:40px"><span class="placeholder">Enter airport, city or zip code</span></div>
  <div class="checkbox"></div>
  <span class="check-text">Return at different location</span>

  <span class="label" style="left:32px;top:161px">Pick-up date</span>
  <span class="label" style="left:136px;top:161px">Time</span>
  <span class="label" style="left:200px;top:161px">Drop-off date</span>
  <span class="label" style="left:304px;top:161px">Time</span>
  <div class="field" style="left:32px;top:179px;width:96px;height:40px">
    <svg class="abs" style="left:11px;top:14px" width="11" height="11" viewBox="0 0 11 11" aria-hidden="true"><rect x="0.5" y="1.5" width="10" height="9" fill="none" stroke="#333"/><rect x="0.5" y="1.5" width="10" height="2.5" fill="#333"/><path d="M3 6h1M5 6h1M7 6h1M3 8h1M5 8h1M7 8h1" stroke="#333"/></svg>
  </div>
  <div class="field" style="left:136px;top:179px;width:48px;height:40px"></div>
  <div class="field" style="left:200px;top:179px;width:96px;height:40px">
    <svg class="abs" style="left:11px;top:14px" width="11" height="11" viewBox="0 0 11 11" aria-hidden="true"><rect x="0.5" y="1.5" width="10" height="9" fill="none" stroke="#333"/><rect x="0.5" y="1.5" width="10" height="2.5" fill="#333"/><path d="M3 6h1M5 6h1M7 6h1M3 8h1M5 8h1M7 8h1" stroke="#333"/></svg>
  </div>
  <div class="field" style="left:304px;top:179px;width:48px;height:40px"></div>

  <span class="label" style="left:32px;top:241px">Car type</span>
  <div class="field" style="left:32px;top:258px;width:96px;height:40px">
    <span class="select-text">Standard</span>
    <svg class="abs" style="left:80px;top:17px" width="8" height="5" aria-hidden="true"><path d="M0 0h8L4 5z" fill="#bbb"/></svg>
  </div>
  <div class="continue">CONTINUE <svg width="5" height="8" aria-hidden="true"><path d="M0 0l5 4-5 4z" fill="#fff"/></svg></div>
</section>

<div class="abs divider"></div>

<div class="abs welcome-head"><h1>Welcome to Quarvin</h1></div>
<div class="abs welcome-text">
  <p>As Dubai is expected to welcome millions of tourists and visitors, car rental industry is believed to escalate more rapidly in the region.</p>
  <p>Over the past five years, demands for car rentals in Dubai has been augmenting at a healthy pace and is currently registering a growth rate of 20 to 25 percent per year. The swift economic growth and the number.....</p>
  <p style="margin-top:4px;text-align:right;padding-right:5px"><span class="read-more">read more [+]</span></p>
</div>

<section class="abs mission">
  <h2>Mission &amp; Vision</h2>
  <div class="mission-rule"></div>
  <div class="mission-photo" role="img" aria-label="Photograph of car keys being handed over in front of a silver hatchback"></div>
  <p class="mission-text">To be one of the leading auto leasing company in<br>the fast growing economy and tourism industry of the<br>emirate of Dubai and play alongside....</p>
  <span class="read-more">read more [+]</span>
</section>

<div class="abs footer-band"></div>
<div class="abs socials">
  <span class="social" aria-label="Social link"></span>
  <span class="social" aria-label="Social link"></span>
  <span class="social" aria-label="Social link"></span>
  <span class="social" aria-label="Social link"></span>
  <span class="social" aria-label="Email">
    <svg width="18" height="13" viewBox="0 0 18 13" aria-hidden="true"><rect x="0.75" y="0.75" width="16.5" height="11.5" fill="none" stroke="#fff" stroke-width="1.5"/><path d="M1 1l8 6.5L17 1" fill="none" stroke="#fff" stroke-width="1.5"/></svg>
  </span>
</div>
<nav class="abs footer-nav">
  <span>Home</span><span class="sep">|</span><span>About Us</span><span class="sep">|</span><span>Our Team</span><span class="sep">|</span><span>Strategy</span><span class="sep">|</span><span>Contact Us</span>
</nav>
<p class="abs copyright">© Copyright 2015, Quarvin. All rights reserved.</p>

</body>
</html>
```